Tarnby Group letterhead

Hi,

I need a letterhead template created for our business. This should be done in word format and A4 size. The images need to not move in the template ie when I am adding writing in etc. and should flow on when I get to a second page.

I have attached our logo templates below.

Other details to include on the letterhead somewhere are:

0438 915 267
Max@Tarnbyelectrical.example.au
PO Box 817 Marrowvale NSW 2190
ABN: 57 318 962 407

Thanks!

```html
<!DOCTYPE html>
<html lang="en">
<head>
<meta charset="utf-8">
<title>Tarnby Group letterhead</title>
<link href="https://fonts.googleapis.com/css2?family=Montserrat:wght@400;500;800&display=swap" rel="stylesheet">
<style>
  :root {
    --backdrop: #d3d3d3;
    --paper: #ffffff;
    --ink: #1b1b1b;
    --text: #4a4a4a;
    --accent: #f25106;
    --watermark: #ececec;
  }
  * { margin: 0; padding: 0; box-sizing: border-box; }
  html, body { width: 1200px; height: 903px; overflow: hidden; }
  body {
    background: var(--backdrop);
    font-family: "Montserrat", sans-serif;
    position: relative;
  }
  .sheet {
    position: absolute;
    top: 144px;
    width: 435px;
    height: 615px;
    background: var(--paper);
    box-shadow: 0 1px 3px rgba(0,0,0,0.18);
    overflow: hidden;
  }
  .sheet--first { left: 139px; }
  .sheet--second { left: 626px; }

  .brand {
    position: absolute;
    top: 74px;
    right: 36px;
    font-weight: 800;
    font-size: 12px;
    letter-spacing: 0.6px;
    text-transform: uppercase;
    color: var(--accent);
    white-space: nowrap;
  }

  .watermark {
    position: absolute;
    left: 0;
    right: 0;
    top: 300px;
    text-align: center;
    font-weight: 800;
    font-size: 38px;
    letter-spacing: 1px;
    text-transform: uppercase;
    color: var(--watermark);
    white-space: nowrap;
  }

  .footer {
    position: absolute;
    left: 33px;
    right: 36px;
    top: 532px;
    border-top: 1.2px solid var(--accent);
    padding-top: 10px;
    display: flex;
    justify-content: space-between;
    font-size: 8px;
    line-height: 10px;
    color: var(--text);
  }
  .contact { list-style: none; }
  .contact li { display: flex; align-items: center; gap: 5px; }
  .contact svg { width: 6px; height: 6px; fill: var(--accent); flex: none; }
  .address { font-style: normal; text-align: right; }

  .edge-bar {
    position: absolute;
    left: 0;
    right: 0;
    bottom: 0;
    height: 7px;
    display: flex;
    gap: 3px;
  }
  .edge-bar__dark { flex: 0 0 358px; background: var(--ink); }
  .edge-bar__accent { flex: 1; background: var(--accent); }

  .page-label {
    position: absolute;
    top: 790px;
    width: 435px;
    text-align: center;
    font-size: 10px;
    font-weight: 500;
    letter-spacing: 1.4px;
    color: var(--ink);
  }
  .page-label--first { left: 139px; }
  .page-label--second { left: 626px; }
</style>
</head>
<body>

<section class="sheet sheet--first">
  <header class="brand">Tarnby Group</header>

  <div class="watermark" aria-hidden="true">Tarnby Group</div>

  <footer class="footer">
    <ul class="contact">
      <li>
        <svg viewBox="0 0 10 10" aria-hidden="true"><path d="M2 0.5 L3.6 2.8 L2.6 3.8 Q3.8 6.2 6.2 7.4 L7.2 6.4 L9.5 8 L8.2 9.5 Q3.5 9 0.5 1.8 Z"/></svg>
        0438 915 267
      </li>
      <li>
        <svg viewBox="0 0 10 10" aria-hidden="true"><path d="M0 2 H10 V8.5 H0 Z" /><path d="M0 2 L5 5.6 L10 2" stroke="#fff" stroke-width="0.9" fill="none"/></svg>
        Max@Tarnbyelectrical.example.au
      </li>
      <li>
        <svg viewBox="0 0 10 10" aria-hidden="true"><circle cx="5" cy="5" r="4.6"/><path d="M5 0.6 V9.4 M0.6 5 H9.4" stroke="#fff" stroke-width="0.8"/></svg>
        Tarnbyelectrical.example.au
      </li>
    </ul>
    <address class="address">
      PO Box 817<br>
      Marrowvale, NSW 2190<br>
      ABN: 57 318 962 407
    </address>
  </footer>

  <div class="edge-bar">
    <span class="edge-bar__dark"></span>
    <span class="edge-bar__accent"></span>
  </div>
</section>

<section class="sheet sheet--second">
  <div class="watermark" aria-hidden="true">Tarnby Group</div>
</section>

<p class="page-label page-label--first">PAGE 01</p>
<p class="page-label page-label--second">PAGE 02</p>

</body>
</html>
```